依頼詳細
お店の看板デザインを依頼させて頂きます。
看板は国道沿いに2つ、裏通りに1つ、スタンド看板1つを設置予定です。
スクールと共にサロン・ショップも展開している事が分かり、印象に残る様なデザインを希望します。
宜しくお願いいたします。
記載項目
記載項目:電話番号 ・ロゴ・URL
ロゴはこちらのサイトで依頼、選定済(添付いたします)
URL 後日取得予定
看板は南北に走る国道に、北向きと西向きに一枚ずつ、裏通り東向きに一枚、スタンド看板の設置場所はお店の前か、国道から見える位置に置く予定です。

看板サイズ:国道沿い   H 2000 x W 1000 / H 2440 x W 1220
裏通り    H 910 x W 1820
スタンド看板 H 1300 x W 600
希望イメージ
シンプル 複雑
単色 カラフル
暗い 明るい
日常 高級
遊び心 厳粛
未来的 伝統的
女性的 男性的
希望する色
清潔、エレガント、高級なイメージを考えています
納品ファイル
• 高解像度JPG (.jpg)
• イラストレーター形式 (.ai)
• フォトショップ形式 (.psd)
補足説明
看板のデザインは縦型のもの1点でお願いします。
色はえんじ色でお願いします。

アロマテラピー(Aromatherapy)の文字を入れて頂き
アロマスクール(Aroma School)
ボディ&フェイシャル サロン(Body&Facial Salon)
アロマショップ(Aroma shop)
と入れて頂きたいです。
文字は英語でもカタカナでも両方使って頂いても構いません。

どうぞ宜しくお願いします。
たくさんのご提案ありがとうございます。

デザインの色ですが、えんじ色でと指定しておりましたが
ランサーさんからのご意見で、エレガント・高級感なら茶系が良いのでは…
とアドバイスいただきました。
確かにそうかもしれません。
私どもは素人ですので、プロの方のアドバイスは大変ありがたいです。

ですので、色はえんじには拘りません。
えんじを含め、他の色でも自由にデザインお願い致します。

どうぞ宜しくお願い致します。
たくさんの良いご提案をありがとうございます。

ご提案を拝見させて頂き、漠然としていたものが
だんだんと具体的にイメージ出来る様になって参りました。

前回、入れて頂きたい文言を挙げさせて頂きましたが
今回訂正し、以下のものを入れて頂きたいと思います。

Beauty&Body School
エステ・アロマテラピー・リフレクソロジー・ボディケア
Beauty&Body Salon
エステ・オイルトリートメント・リフレクソロジー・アロマテラピー
Aroma Shop
エッセンシャルオイル・ナチュラルオイル・ハーブウォーター

カタカナは英語よりも小さめでお願い致します。
字体はお任せいたします。

度々の追記で申し訳ありませんが、どうぞ宜しくお願い致します。
■ 選んだ理由

デザインの全体的なイメージが一つに偏らず、エステ・スクール・ショップのそれぞれにリンクしていた事。

縦長の看板がより良く生かされたデザインも気に入りました。

■ 提案者全員のお礼・コメント

ご提案下さったランサーの皆さま、大変ありがとうございました。

たくさんのご提案に感謝致します。
また、機会がございましたら宜しくお願い致します。

```html
<!DOCTYPE html>
<html lang="ja">
<head>
<meta charset="utf-8">
<title>LUNE Beauty &amp; Body balance – Sign</title>
<link rel="stylesheet" href="https://fonts.googleapis.com/css2?family=Cormorant+Garamond:wght@500;600;700&family=Noto+Sans+JP:wght@400&display=swap">
<style>
  :root {
    --wine-deep: #6e1419;
    --wine: #8e2428;
    --wine-soft: #a8413c;
    --cream: #f6ead9;
    --cream-light: #fbf4ea;
    --gold: #d9b56e;
    --gold-bright: #ecb447;
    --text-light: #f7ecdd;
    --text-wine: #7b1d22;
    --rule: rgba(233, 196, 140, 0.55);
  }
  * { margin: 0; padding: 0; box-sizing: border-box; }
  html, body { width: 1200px; height: 2320px; overflow: hidden; }
  body { background: #ffffff; }
  .sign {
    position: relative;
    width: 1200px;
    height: 2320px;
    overflow: hidden;
    background: linear-gradient(180deg,
      var(--wine-deep) 0%,
      var(--wine) 30%,
      var(--wine-soft) 52%,
      #c98a78 62%,
      var(--cream) 74%,
      var(--cream-light) 100%);
    font-family: "Cormorant Garamond", "Times New Roman", serif;
  }
  .brand {
    position: absolute;
    top: 220px;
    left: 0;
    width: 100%;
    text-align: center;
    color: var(--gold);
  }
  .brand-name {
    font-size: 230px;
    font-weight: 500;
    letter-spacing: 18px;
    line-height: 1;
  }
  .brand-tagline {
    margin-top: 24px;
    font-size: 60px;
    font-weight: 500;
    line-height: 1;
    letter-spacing: 1px;
  }
  .rule {
    position: absolute;
    left: 140px;
    width: 920px;
    height: 2px;
    background: var(--rule);
  }
  .service {
    position: absolute;
    left: 0;
    width: 100%;
    text-align: center;
    color: var(--text-light);
  }
  .service-title {
    font-size: 102px;
    font-weight: 500;
    line-height: 1;
    letter-spacing: -1px;
  }
  .service-title .accent {
    color: var(--gold-bright);
    font-weight: 700;
  }
  .service-menu {
    margin-top: 16px;
    font-family: "Noto Sans JP", sans-serif;
    font-size: 28px;
    font-weight: 400;
    letter-spacing: 0;
    line-height: 1;
  }
  .shop-title {
    display: flex;
    justify-content: center;
    align-items: center;
    gap: 22px;
  }
  .shop-visual {
    width: 150px;
    height: 84px;
    border-radius: 50%;
    background: radial-gradient(ellipse at center, #f2c25a 0%, #d14a7a 45%, #8a2a66 80%, rgba(138,42,102,0) 100%);
  }
  .feature-visual {
    position: absolute;
    left: 140px;
    top: 1330px;
    width: 920px;
    height: 510px;
    border-radius: 50%;
    background: radial-gradient(ellipse at 55% 45%, #f6e2cf 0%, #e9c6a8 45%, #c98a6e 75%, rgba(246,234,217,0.4) 100%);
    box-shadow: 0 0 40px 24px rgba(251,244,234,0.9);
  }
  .contact {
    position: absolute;
    left: 0;
    width: 100%;
    text-align: center;
    color: var(--text-wine);
  }
  .contact-phone {
    top: 2040px;
    display: flex;
    justify-content: center;
    align-items: center;
    gap: 22px;
    font-size: 100px;
    font-weight: 500;
    line-height: 1;
    letter-spacing: 2px;
  }
  .tel-badge {
    display: inline-flex;
    align-items: center;
    justify-content: center;
    width: 108px;
    height: 68px;
    border: 4px solid var(--text-wine);
    border-radius: 50%;
    font-size: 36px;
    font-weight: 600;
    letter-spacing: 0;
  }
  .contact-web {
    top: 2164px;
    font-size: 54px;
    font-weight: 600;
    letter-spacing: 6px;
    line-height: 1;
  }
</style>
</head>
<body>
  <main class="sign">
    <header class="brand">
      <div class="brand-name">LUNE</div>
      <div class="brand-tagline">Beauty &amp; Body balance</div>
    </header>

    <div class="rule" style="top:650px"></div>

    <section class="service" style="top:700px">
      <h2 class="service-title">Beauty &amp; Body <span class="accent">School</span></h2>
      <p class="service-menu">エステ・アロマテラピー・リフレクソロジー・ボディケア</p>
    </section>

    <div class="rule" style="top:880px"></div>

    <section class="service" style="top:910px">
      <h2 class="service-title">Beauty &amp; Body <span class="accent">Salon</span></h2>
      <p class="service-menu">エステ・オイルトリートメント・リフレクソロジー・アロマテラピー</p>
    </section>

    <div class="rule" style="top:1090px"></div>

    <section class="service" style="top:1122px">
      <h2 class="service-title shop-title">
        <span class="shop-visual" role="img" aria-label="Aroma candle with flower petals"></span>
        <span>Aroma <span class="accent">Shop</span></span>
      </h2>
      <p class="service-menu">エッセンシャルオイル・ナチュラルオイル・ハーブウォーター</p>
    </section>

    <div class="feature-visual" role="img" aria-label="Photo of a relaxed woman receiving a facial treatment with flowers beside her"></div>

    <div class="contact contact-phone">
      <span class="tel-badge">TEL</span>
      <span>012-345-6789</span>
    </div>
    <div class="contact contact-web">www.lune-beauty.com</div>
  </main>
</body>
</html>
```